ORVA CRM website - sleek, sophisticated, uplifting

ORVA Center for Regenerative Medicine is a cutting-edge medical clinic aimed at providing treatment for various chronic conditions and help people stave off the declines usually associated with aging. We utilize the latest technology in regenerative medicine to help people with autoimmune conditions, musculoskeletal problems and chronic pain, neurodegenerative conditions, male enhancement, facial rejuvenation and hair restoration, etc. We provide personalized medicine, through highly compassionate and competent doctors and staff.

please look at my current website which is not focused on regenerative medicine, but some contents can stay, as far as the philosophy of the treatment: www.plmwellnessgroup.example. But the reason I am changing the name of the clinic is because the focus of the medical practice is shifted entirely to "regenerative medicine" - using the body's own healing mechanism such as stem cells and growth factors...

Please DO NOT recycle old graphics and pictures. I want this site to be brand new, fresh and original.

Would like the website to be more sophisticated and nicer-looking than this website: www.vantrelo.example

Target Market(s)

People who care a great deal about their health (above age 35), wants to prevent declines in their looks and health as they are getting older. Generally high income sector of the society that can afford self-pay (no insurance accepted) expensive stem cell treatment ranging from $4000 to $20,000.

Industry/Entity Type

Healthcare

Coding

Coded - Design and coding required

Number of Pages Required

5+ page

Font styles to use
Sans Serif
Other font styles liked:
• Al Bayan, Avenir, Didot, Open Sans or Tsukushi A Round Gothic for central text, but may use Chalkboard for titles, or others as seen fit

Colors

Designer to choose colors to be used in the design.

Requirements
Must have
• Ultra modern look, very clean & sleek images and layout, portraying a sense of sophistication and confidence. Works beautifully well with existing logo. Give a sense that the clinic employs cutting-edge science, and provide highly competent & compassionate services.
• More sophisticated and nicer-looking than this website: www.vantrelo.example
Nice to have
• many pages and links to science articles
Should not have
• fonts too playful or hard to read.

```html
<!DOCTYPE html>
<html lang="en">
<head>
<meta charset="utf-8">
<title>ORVA Center for Regenerative Medicine</title>
<link href="https://fonts.googleapis.com/css2?family=Merriweather:wght@400;700&family=Open+Sans:wght@400;600;700&display=swap" rel="stylesheet">
<style>
:root{
  --gold:#c9992e;
  --ink:#1b1b1b;
  --text:#555555;
  --muted:#8a8a8a;
  --grey-band:#e6e7e8;
  --line:#b9b9b9;
  --black:#0c0c0c;
  --white:#ffffff;
}
*{margin:0;padding:0;box-sizing:border-box}
html,body{width:1200px;height:2941px;overflow:hidden;background:var(--white)}
body{position:relative;font-family:"Open Sans",Arial,sans-serif;color:var(--text)}
.abs{position:absolute}
.serif{font-family:"Merriweather",Georgia,serif}

/* hero */
.hero-photo{left:0;top:0;width:1200px;height:540px;
  background:radial-gradient(ellipse at 70% 35%,#6e6e6e 0%,#3c3c3c 40%,#1e1e1e 80%);}
.diagonal{left:0;top:0}
.nav a{position:absolute;top:66px;font-size:10px;font-weight:700;color:var(--white);text-decoration:none;letter-spacing:.3px}
.nav a.active{color:var(--gold)}
.caret{position:absolute;width:0;height:0;border-left:4px solid transparent;border-right:4px solid transparent;border-bottom:5px solid var(--gold)}
.brand{left:540px;top:28px;width:120px;text-align:center}
.brand-dot{display:block;margin:0 auto 8px;width:34px;height:34px;border-radius:50%;background:var(--gold)}
.brand-name{font-size:30px;font-weight:700;color:var(--white);letter-spacing:2px;line-height:1}
.hero-title{left:0;width:1200px;top:276px;text-align:center;font-size:30px;font-weight:400;color:var(--white);letter-spacing:.5px}
.hero-title span{color:var(--gold);font-weight:700}
.hero-lead{left:330px;width:540px;top:320px;text-align:center;font-size:12px;line-height:21px;color:#e6e6e6}
.dots{left:942px;top:281px;width:12px}
.dots i{display:block;width:9px;height:9px;border-radius:50%;border:1px solid #dcdcdc;margin-bottom:5px}
.dots i.on{background:var(--gold);border-color:var(--gold);width:10px;height:10px}

.video{left:294px;top:453px;width:612px;height:337px;
  background:linear-gradient(135deg,#8a1d2b 0%,#d05a76 35%,#e98aa0 55%,#2fb5c0 75%,#7a1e33 100%);
  box-shadow:0 22px 30px -14px rgba(0,0,0,.45)}
.play{left:568px;top:594px;width:64px;height:64px;border-radius:50%;background:rgba(255,255,255,.92)}
.play:after{content:"";position:absolute;left:26px;top:20px;border-left:18px solid var(--gold);border-top:12px solid transparent;border-bottom:12px solid transparent}
.video-note{left:330px;width:540px;top:810px;text-align:center;font-size:12px;line-height:20px}
.video-note b{color:var(--ink)}

/* section heads */
.kicker{left:0;width:1200px;text-align:center;font-size:12px;color:var(--ink);letter-spacing:.5px}
.section-title{left:0;width:1200px;text-align:center;font-size:27px;font-weight:700;color:var(--ink);letter-spacing:.5px}
.rule{left:560px;width:80px;height:2px;background:var(--gold)}
.section-lead{left:0;width:1200px;text-align:center;font-size:11px}

/* services */
.services-bg{left:0;top:886px;width:1200px;height:598px;
  background:radial-gradient(ellipse at 20% 40%,#e2e2e2 0%,#f4f4f4 45%,#fbfbfb 80%)}
.grid-line{background:var(--line)}
.service{width:230px;text-align:center}
.service svg{display:block;margin:0 auto}
.service h3{margin-top:10px;font-size:11px;font-weight:700;color:var(--ink)}
.service p{margin-top:6px;font-size:10.5px;line-height:17px;color:var(--muted)}

/* about */
.about-bg{left:0;top:1484px;width:1200px;height:353px;background:var(--grey-band)}
.about-col{width:334px;font-size:10px;line-height:16px;color:#444}
.about-col b{color:var(--ink)}
.more{left:0;width:1200px;text-align:center;font-size:13px;font-weight:700;color:var(--gold);letter-spacing:.5px}

/* blog */
.blog-bg{left:0;width:1200px;
  background:radial-gradient(ellipse at 50% 70%,#ececec 0%,#f7f7f7 50%,#fdfdfd 85%)}
.card{width:206px}
.card-photo{width:206px;height:167px}
.card h4{margin-top:22px;font-family:"Merriweather",Georgia,serif;font-size:11.5px;line-height:18px;color:var(--ink)}
.card .meta{margin-top:4px;font-size:9.5px;color:#444}
.card .meta span{display:inline-block;margin:0 8px;color:#999}
.card p{margin-top:6px;font-size:10.5px;line-height:18px;color:#555}

/* contact */
.contact-bg{left:0;top:2441px;width:1200px;height:374px;background:var(--black)}
.contact-title{left:0;width:1200px;top:2481px;text-align:center;font-size:26px;font-weight:400;color:var(--white)}
.contact-lead{left:0;width:1200px;top:2526px;text-align:center;font-size:11px;color:#ddd}
.field{border:1px solid #8c8c8c;border-radius:2px;color:#ddd;font-size:9.5px;padding:11px 10px}
.submit{left:0;width:1200px;top:2750px;text-align:center;font-size:13px;font-weight:700;color:var(--gold);letter-spacing:.5px}

/* footer */
.foot-nav a{position:absolute;top:2853px;font-size:9.5px;font-weight:600;color:var(--ink);text-decoration:none}
.foot-nav a.active{color:var(--gold)}
.copy{left:249px;top:2890px;font-size:9px;line-height:15px;color:#444}
.social{width:40px;height:40px;border:2px solid var(--gold);border-radius:50%}
.foot-brand{left:856px;top:2835px;width:100px;text-align:center}
.foot-brand .brand-dot{width:28px;height:28px;margin-bottom:6px}
.foot-brand .brand-name{color:var(--ink);font-size:26px}
</style>
</head>
<body>

<!-- HERO -->
<div class="abs hero-photo" role="img" aria-label="Black and white photo of a gloved scientist working with a microscope in a lab"></div>
<svg class="abs diagonal" width="1200" height="700" viewBox="0 0 1200 700" aria-hidden="true">
  <defs><linearGradient id="fade" x1="0" y1="0" x2="0" y2="1"><stop offset="0" stop-color="#ffffff"/><stop offset="1" stop-color="#f1f1f1"/></linearGradient></defs>
  <polygon points="0,540 1200,421 1200,700 0,700" fill="#ffffff"/>
  <polygon points="0,540 1200,421 1200,540 0,657" fill="#c9992e"/>
  <polygon points="0,657 1200,540 1200,700 0,700" fill="url(#fade)"/>
</svg>
<div class="abs" style="left:0;top:700px;width:1200px;height:186px;background:linear-gradient(#f6f6f6,#f1f1f1)"></div>

<nav class="nav">
  <a class="active" href="#" style="left:249px">HOME</a>
  <span class="caret" style="left:258px;top:84px"></span>
  <a href="#" style="left:307px">VIDEO</a>
  <a href="#" style="left:363px">SERVICES</a>
  <a href="#" style="left:762px">ABOUT US</a>
  <a href="#" style="left:839px">BLOG</a>
  <a href="#" style="left:890px">CONTACT US</a>
</nav>
<div class="abs brand"><span class="brand-dot"></span><div class="brand-name">ORVA</div></div>

<h1 class="abs hero-title serif">MULTI-FACETED <span>HEALTH</span></h1>
<p class="abs hero-lead">Lorem Ipsum has been the industry's standard dummy text ever since the 1500s, when an unknown printer took a galley of type and scrambled it to make a type specimen book.</p>
<div class="abs dots"><i></i><i></i><i></i><i class="on"></i></div>

<div class="abs video" role="img" aria-label="Video still of a 3D medical illustration of blood vessels and tissue"></div>
<div class="abs play" aria-label="Play video"></div>
<p class="abs video-note"><b>Lorem Ipsum</b> has been the industry's standard dummy text ever since the when an unknown printer took a galley of type and scrambled it to make a type specimen book.</p>

<!-- SERVICES -->
<div class="abs services-bg" role="img" aria-label="Faint black and white photo of doctors at work"></div>
<div class="abs kicker" style="top:931px">SERVICES</div>
<h2 class="abs section-title serif" style="top:948px">LOREM IPSUM</h2>
<div class="abs rule" style="top:988px"></div>
<p class="abs section-lead" style="top:1001px">Lorem ipsum is simply dummy text of the printing and typesetting industry.</p>

<div class="abs grid-line" style="left:478px;top:1058px;width:1px;height:357px"></div>
<div class="abs grid-line" style="left:721px;top:1058px;width:1px;height:357px"></div>
<div class="abs grid-line" style="left:249px;top:1239px;width:702px;height:1px"></div>

<div class="abs service" style="left:248px;top:1060px">
  <svg width="66" height="66" viewBox="0 0 66 66" fill="none" stroke="#c9992e" stroke-width="2"><rect x="24" y="26" width="36" height="26" rx="3"/><path d="M35 26v-5h14v5M42 33v12M36 39h12"/><path d="M10 14v30M6 20h8M6 28h8M6 36h8"/></svg>
  <h3>Lorem Ipsum</h3><p>Lorem Ipsum is simply dummy text of the printing and typesetting industry.</p>
</div>
<div class="abs service" style="left:485px;top:1060px">
  <svg width="66" height="66" viewBox="0 0 66 66" fill="none" stroke="#c9992e" stroke-width="2"><rect x="22" y="8" width="22" height="7" rx="2"/><rect x="18" y="15" width="30" height="40" rx="4"/><path d="M24 34h18M26 30v8M40 30v8"/></svg>
  <h3>Lorem Ipsum</h3><p>Lorem Ipsum is simply dummy text of the printing and typesetting industry.</p>
</div>
<div class="abs service" style="left:721px;top:1060px">
  <svg width="66" height="66" viewBox="0 0 66 66" fill="none" stroke="#c9992e" stroke-width="2"><path d="M33 8v50M14 20h38M22 30h22M24 42h18"/><circle cx="33" cy="8" r="3"/></svg>
  <h3>Lorem Ipsum</h3><p>Lorem Ipsum is simply dummy text of the printing and typesetting industry.</p>
</div>
<div class="abs service" style="left:248px;top:1245px">
  <svg width="66" height="66" viewBox="0 0 66 66" fill="none" stroke="#c9992e" stroke-width="2"><ellipse cx="33" cy="33" rx="24" ry="9"/><ellipse cx="33" cy="33" rx="24" ry="9" transform="rotate(60 33 33)"/><ellipse cx="33" cy="33" rx="24" ry="9" transform="rotate(120 33 33)"/><circle cx="33" cy="33" r="3"/></svg>
  <h3>Lorem Ipsum</h3><p>Lorem Ipsum is simply dummy text of the printing and typesetting industry.</p>
</div>
<div class="abs service" style="left:485px;top:1245px">
  <svg width="66" height="66" viewBox="0 0 66 66" fill="none" stroke="#c9992e" stroke-width="2"><rect x="16" y="10" width="34" height="46" rx="3"/><rect x="26" y="6" width="14" height="8" rx="2"/><path d="M20 36h7l4-8 5 14 4-6h6"/></svg>
  <h3>Lorem Ipsum</h3><p>Lorem Ipsum is simply dummy text of the printing and typesetting industry.</p>
</div>
<div class="abs service" style="left:721px;top:1245px">
  <svg width="66" height="66" viewBox="0 0 66 66" fill="none" stroke="#c9992e" stroke-width="2"><path d="M27 8h12M29 8v16a16 16 0 1 0 8 0V8"/><path d="M19 40h28"/></svg>
  <h3>Lorem Ipsum</h3><p>Lorem Ipsum is simply dummy text of the printing and typesetting industry.</p>
</div>

<!-- ABOUT -->
<div class="abs about-bg"></div>
<svg class="abs" style="left:0;top:1700px" width="1200" height="260" viewBox="0 0 1200 260" aria-hidden="true">
  <polygon points="0,10 1200,133 1200,250 0,137" fill="#c9992e"/>
  <polygon points="0,137 1200,250 1200,260 0,260" fill="#fcfcfc"/>
</svg>
<div class="abs kicker" style="top:1529px">ABOUT US</div>
<h2 class="abs section-title serif" style="top:1546px">REGENERATIVE MEDICINE</h2>
<p class="abs about-col" style="left:249px;top:1614px"><b>Lorem Ipsum</b> is simply dummy text of the printing and typesetting industry. Lorem Ipsum has been the industry's standard dummy text ever since the 1500s, when an unknown printer took a galley of type and scrambled it to make a type specimen book.</p>
<p class="abs about-col" style="left:617px;top:1614px"><b>It</b> has survived not only five centuries, but also the leap into electronic typesetting, remaining essentially unchanged. It was popularised in the 1960s with the release of Tessaline sheets containing Lorem Ipsum passages, and more recently with desktop publishing software like Corvin LayoutDesk including versions of Lorem Ipsum.</p>
<div class="abs more serif" style="top:1726px">READ MORE</div>
<span class="caret" style="left:596px;top:1748px"></span>

<!-- BLOG -->
<div class="abs blog-bg" style="top:1960px;height:481px" role="img" aria-label="Faint photo of a stethoscope on a desk"></div>
<div class="abs kicker" style="top:1899px">BLOG</div>
<h2 class="abs section-title serif" style="top:1914px">MEDICINE</h2>
<div class="abs rule" style="top:1955px"></div>
<p class="abs section-lead" style="top:1968px">Lorem Ipsum is simply dummy text of the printing and typesetting industry.</p>

<article class="abs card" style="left:249px;top:2015px">
  <div class="card-photo" role="img" aria-label="Photo of hands filling out a medical form at a desk" style="background:linear-gradient(135deg,#dfe7ee,#b9c6d0 60%,#8f9ba6)"></div>
  <h4>Lorem Ipsum is simply dummy text of the printing and typesetting.</h4>
  <div class="meta">Community<span>|</span>No Comments</div>
  <p>Lorem Ipsum has been the industry's standard dummy text ever since the 1500s, when an unknown printer took a galley of type and scrambled.</p>
</article>
<article class="abs card" style="left:496px;top:2015px">
  <div class="card-photo" role="img" aria-label="Photo of a young child holding a white rabbit" style="background:linear-gradient(135deg,#7c9a4a,#c9b48c 55%,#e9dcc7)"></div>
  <h4>Lorem Ipsum is simply dummy text of the printing and typesetting.</h4>
  <div class="meta">Community<span>|</span>No Comments</div>
  <p>Lorem Ipsum has been the industry's standard dummy text ever since the 1500s, when an unknown printer took a galley of type and scrambled.</p>
</article>
<article class="abs card" style="left:745px;top:2015px">
  <div class="card-photo" role="img" aria-label="Photo of a smiling couple outdoors" style="background:linear-gradient(135deg,#b7cc86,#8aa36a 45%,#4e6b8a)"></div>
  <h4>Lorem Ipsum is simply dummy text of the printing and typesetting.</h4>
  <div class="meta">Community<span>|</span>No Comments</div>
  <p>Lorem Ipsum has been the industry's standard dummy text ever since the 1500s, when an unknown printer took a galley of type and scrambled.</p>
</article>
<div class="abs more serif" style="top:2371px">ALL BLOG</div>
<span class="caret" style="left:596px;top:2392px"></span>

<!-- CONTACT -->
<div class="abs contact-bg"></div>
<h2 class="abs contact-title serif">Contact Us</h2>
<p class="abs contact-lead">Lorem Ipsum is simply dummy text of the printing and typesetting industry.</p>
<div class="abs field" style="left:249px;top:2574px;width:345px;height:37px">Your Name</div>
<div class="abs field" style="left:249px;top:2622px;width:345px;height:37px">Your Email</div>
<div class="abs field" style="left:249px;top:2670px;width:345px;height:37px">Subject</div>
<div class="abs field" style="left:606px;top:2574px;width:345px;height:133px">Your Message</div>
<div class="abs submit serif">SUBMIT</div>
<span class="caret" style="left:596px;top:2772px"></span>

<!-- FOOTER -->
<nav class="foot-nav">
  <a class="active" href="#" style="left:249px">HOME</a>
  <a href="#" style="left:300px">VIDEO</a>
  <a href="#" style="left:350px">SERVICES</a>
  <a href="#" style="left:414px">ABOUT US</a>
  <a href="#" style="left:479px">BLOG</a>
  <a href="#" style="left:526px">CONTACT US</a>
</nav>
<p class="abs copy">Copyright © 2018 Kelvora. All rights reserved.</p>
<div class="abs social" style="left:652px;top:2844px" aria-label="Social link"></div>
<div class="abs social" style="left:699px;top:2844px" aria-label="Social link"></div>
<div class="abs social" style="left:746px;top:2844px" aria-label="Social link"></div>
<div class="abs foot-brand"><span class="brand-dot"></span><div class="brand-name">ORVA</div></div>

</body>
</html>
```